Sandwich Board and Poster design promoting a medical aesthetic clinic

I am looking for a clean, modern and relaxing design promoting a medical physician-led aesthetic clinic.
Services offered are neuromodulator treatment (Quelvo) and Dermal Fillers.
Logo must be included.
Use the tag line "Refresh your look, revive your spirit."
Address is 204-205 27361 92 Ave, Surrey, V7K 2M4
604-555-0148
email - info@lumawellpine.ca
www.lumawellpine.ca

```html
<!DOCTYPE html>
<html lang="en">
<head>
<meta charset="utf-8">
<title>Lumawell Pine Poster</title>
<link rel="stylesheet" href="https://fonts.googleapis.com/css2?family=Poppins:wght@400;500;600;800&display=swap">
<style>
  :root {
    --navy: #1f3a5f;
    --navy-deep: #1b3558;
    --gold: #c9a53a;
    --gold-light: #e2c766;
    --cream: #f7f2e0;
    --cream-light: #fbf8ee;
    --ink: #1d1d1d;
    --page: #e9e9e9;
    --hair: #e2d8c0;
    --skin-light: #f0d9c4;
    --skin: #e3bea1;
    --skin-deep: #d4a688;
  }
  * { margin: 0; padding: 0; box-sizing: border-box; }
  html, body { width: 1200px; height: 1200px; overflow: hidden; background: var(--page); font-family: "Poppins", sans-serif; }
  .poster {
    position: absolute; left: 230px; top: 30px; width: 740px; height: 1140px;
    background: linear-gradient(135deg, var(--cream) 0%, var(--cream-light) 55%, #fffdf6 100%);
    overflow: hidden; box-shadow: 0 6px 24px rgba(0,0,0,.15);
  }
  .hero-photo {
    position: absolute; left: 300px; top: 0; width: 440px; height: 823px;
    background:
      linear-gradient(180deg, var(--hair) 0%, var(--hair) 18%, var(--skin-light) 30%, var(--skin) 60%, var(--skin-deep) 100%);
    -webkit-mask-image: linear-gradient(90deg, transparent 0%, #000 22%);
    mask-image: linear-gradient(90deg, transparent 0%, #000 22%);
  }
  .brand {
    position: absolute; left: 10px; top: 196px; width: 300px; text-align: center; white-space: nowrap;
    font-weight: 500; font-size: 25px; letter-spacing: 4px; color: var(--ink);
  }
  .brand-dot { display: inline-block; width: 12px; height: 12px; border-radius: 50%; background: var(--gold); margin-right: 10px; vertical-align: middle; position: relative; top: -2px; }
  .headline {
    position: absolute; left: 47px; top: 292px;
    font-weight: 800; font-size: 44px; line-height: 52px; color: var(--navy); text-transform: uppercase;
  }
  .services-tag {
    position: absolute; left: 43px; top: 530px; width: 252px; height: 34px;
    background: linear-gradient(90deg, var(--gold) 0%, var(--gold-light) 100%);
    clip-path: polygon(0 0, 88% 0, 100% 100%, 0 100%);
    font-weight: 500; font-size: 22px; line-height: 34px; color: var(--navy); padding-left: 8px;
  }
  .services-tag::after {
    content: ""; position: absolute; right: 0; top: 0; width: 24px; height: 34px;
    background: var(--navy); clip-path: polygon(0 0, 40% 0, 100% 100%, 60% 100%);
  }
  .service-list { position: absolute; left: 40px; top: 588px; list-style: none; }
  .service-list li {
    position: relative; padding-left: 28px; font-size: 26px; line-height: 33px; color: var(--ink); margin-bottom: 8px;
  }
  .service-list li::before {
    content: ""; position: absolute; left: 2px; top: 11px; width: 12px; height: 12px; border-radius: 50%;
    background: var(--gold); box-shadow: inset 0 0 0 3px var(--gold), inset 0 0 0 6px var(--navy);
  }
  .gold-band { position: absolute; left: 0; width: 740px; height: 10px; background: linear-gradient(90deg, #b8912a, var(--gold-light), #b8912a); }
  .gold-band.top { top: 823px; }
  .gold-band.bottom { top: 996px; }
  .treatment-row { position: absolute; left: 0; top: 833px; width: 740px; height: 163px; background: var(--gold); }
  .treatment-photo { position: absolute; top: 0; height: 163px; }
  .treatment-photo.one { left: 0; width: 239px; background: linear-gradient(120deg, #c7a48a, #8d6a57 50%, #b9d3e3); }
  .treatment-photo.two { left: 252px; width: 236px; background: linear-gradient(120deg, #4a5da8, #c39a80 55%, #3e3b3a); }
  .treatment-photo.three { left: 501px; width: 239px; background: linear-gradient(120deg, #efe6e2, #e2b9a8 50%, #5a6fc4); }
  .contact-bar {
    position: absolute; left: 0; top: 1006px; width: 740px; height: 134px; background: var(--navy-deep);
    color: #fff; font-size: 20px; text-align: center; padding-top: 24px;
  }
  .contact-line { display: flex; justify-content: center; align-items: center; gap: 12px; height: 30px; margin-bottom: 12px; }
  .contact-item { display: inline-flex; align-items: center; gap: 5px; }
  .contact-item svg { width: 14px; height: 14px; }
</style>
</head>
<body>
<div class="poster">
  <div class="hero-photo" role="img" aria-label="Portrait photo of a woman with short blonde hair touching her face"></div>

  <div class="brand"><span class="brand-dot"></span>LUMAWELL PINE</div>

  <h1 class="headline">Refresh<br>your look,<br>revive<br>your spirit.</h1>

  <div class="services-tag">Services Offered</div>
  <ul class="service-list">
    <li>Neuromodulator<br>treatment (Quelvo)</li>
    <li>Dermal Fillers</li>
  </ul>

  <div class="gold-band top"></div>
  <div class="treatment-row">
    <div class="treatment-photo one" role="img" aria-label="Photo of a forehead injection treatment"></div>
    <div class="treatment-photo two" role="img" aria-label="Photo of a gloved practitioner injecting between the brows"></div>
    <div class="treatment-photo three" role="img" aria-label="Photo of a lip and chin filler treatment"></div>
  </div>
  <div class="gold-band bottom"></div>

  <footer class="contact-bar">
    <div class="contact-line">
      <span class="contact-item">
        <svg viewBox="0 0 14 14"><circle cx="7" cy="7" r="7" fill="#c9a53a"/><path d="M4.5 3.5l1.5 0 .6 1.8-1 .7a5 5 0 0 0 2.4 2.4l.7-1 1.8.6v1.5c-3.5.3-6.3-2.5-6-6z" fill="#1b3558"/></svg>
        604-555-0148
      </span>
      <span class="contact-item">
        <svg viewBox="0 0 14 14"><circle cx="7" cy="7" r="7" fill="#c9a53a"/><rect x="3.5" y="4.5" width="7" height="5" fill="none" stroke="#1b3558" stroke-width="1.2"/><path d="M3.5 4.5l3.5 3 3.5-3" fill="none" stroke="#1b3558" stroke-width="1.2"/></svg>
        info@lumawellpine.ca
      </span>
      <span class="contact-item">
        <svg viewBox="0 0 14 14"><circle cx="7" cy="7" r="7" fill="#c9a53a"/><circle cx="7" cy="7" r="3.6" fill="none" stroke="#1b3558" stroke-width="1.1"/><path d="M3.4 7h7.2M7 3.4c-1.6 2-1.6 5.2 0 7.2M7 3.4c1.6 2 1.6 5.2 0 7.2" fill="none" stroke="#1b3558" stroke-width="1"/></svg>
        www.lumawellpine.ca
      </span>
    </div>
    <div class="contact-line">
      <span class="contact-item">
        <svg viewBox="0 0 14 14"><circle cx="7" cy="7" r="7" fill="#c9a53a"/><path d="M7 3a2.6 2.6 0 0 1 2.6 2.6C9.6 7.6 7 11 7 11S4.4 7.6 4.4 5.6A2.6 2.6 0 0 1 7 3z" fill="#1b3558"/><circle cx="7" cy="5.6" r="1" fill="#c9a53a"/></svg>
        204-205 27361 92 Ave, Surrey, V7K 2M4
      </span>
    </div>
  </footer>
</div>
</body>
</html>
```